Photographer website

This website will contain information to sell the services of marvello tebani an up and coming photographer based in london

Target Market(s)

SME's for corporate head shots
mums for kids parties
actors - for headshots
up and coming models

Industry/Entity Type

Photographer

Number of Pages Required

3 page

Requirements
Must have
• Home
• About me
• Contact me
• Portfolio or gallery

```html
<!DOCTYPE html>
<html lang="en">
<head>
<meta charset="utf-8">
<title>marvello tebani — Photographer</title>
<link href="https://fonts.googleapis.com/css2?family=Open+Sans:wght@400;600;700&display=swap" rel="stylesheet">
<style>
:root{
  --pink:#e8415f;
  --pink-deep:#c4324e;
  --ink:#1c1c1c;
  --text:#555;
  --line:#cfcfcf;
  --track:#e4e4e4;
  --footer:#232323;
  --footer-text:#6f6f6f;
  --icon:#8a8a8a;
  --white:#fff;
}
*{box-sizing:border-box;margin:0;padding:0}
html,body{width:1200px;height:2748px;overflow:hidden}
body{position:relative;font-family:"Open Sans",Arial,sans-serif;color:var(--ink);background:var(--white)}
.abs{position:absolute}

/* header */
.site-header{position:absolute;left:0;top:0;width:1200px;height:70px;background:var(--white);box-shadow:0 2px 4px rgba(0,0,0,.12);z-index:2}
.brand{position:absolute;left:84px;top:18px;font-size:22px;font-weight:400;color:var(--ink);letter-spacing:.5px}
.main-nav a{position:absolute;top:0;height:70px;line-height:72px;font-size:15.5px;font-weight:600;color:var(--ink);text-decoration:none;text-transform:uppercase;white-space:nowrap}
.main-nav a.active{background:var(--pink);color:var(--white);left:462px;width:70px;text-align:center}
.social{position:absolute;width:28px;height:28px;border-radius:50%;background:var(--icon)}

/* hero */
.hero{position:absolute;left:0;top:70px;width:1200px;height:503px;background:linear-gradient(100deg,#c5ccd6 0%,#d6dbe2 40%,#b9c2cd 75%,#a9b3bf 100%)}
.hero-tagline{position:absolute;left:84px;top:162px;font-size:32px;font-weight:600;letter-spacing:2px;color:#2b2b2b;white-space:nowrap}
.hero-title{position:absolute;left:82px;top:200px;font-size:62px;font-weight:700;color:var(--pink-deep);letter-spacing:1px;white-space:nowrap}
.hero-dot{position:absolute;top:476px;width:13px;height:13px;border-radius:50%;background:var(--white)}

/* sections */
.section-title{position:absolute;font-size:29px;font-weight:700;letter-spacing:1.5px;color:var(--ink);text-transform:uppercase;white-space:nowrap}
.section-title::after{content:"";position:absolute;left:0;bottom:-6px;width:100%;height:3px;background:var(--pink)}
.section-title.center::after{left:50%;width:110px;margin-left:-55px}
.about-lead{position:absolute;left:86px;top:662px;width:520px;font-size:18px;font-weight:700;line-height:22px}
.about-copy{position:absolute;left:86px;width:470px;font-size:12.5px;line-height:18px;color:var(--text)}

.skill-label{position:absolute;left:661px;font-size:18px;font-weight:600;white-space:nowrap}
.skill-track{position:absolute;left:661px;width:486px;height:11px;background:var(--track)}
.skill-fill{height:100%;background:var(--pink)}
.skill-tip{position:absolute;top:-26px;width:26px;height:17px;margin-left:-13px;background:var(--ink);color:var(--white);font-size:9px;font-weight:700;text-align:center;line-height:17px}

.filter{position:absolute;top:1042px;height:24px;line-height:20px;padding:0 6px;border:2px solid var(--pink);font-size:14px;font-weight:600;white-space:nowrap}
.filter.active{background:var(--pink);color:var(--white)}

.tile{position:absolute}

/* contact */
.field-label{position:absolute;left:132px;font-size:12px;color:var(--text)}
.field-line{position:absolute;left:132px;width:469px;height:1px;background:var(--line)}
.send-btn{position:absolute;left:132px;top:2427px;width:108px;height:30px;border-radius:3px;background:var(--pink);color:var(--white);font-size:14px;text-align:center;line-height:30px}
.map{position:absolute;left:687px;top:2171px;width:394px;height:284px;background:linear-gradient(135deg,#e9e5dc,#dcd9d2)}

/* footer */
.site-footer{position:absolute;left:0;top:2537px;width:1200px;height:211px;background:var(--footer)}
.footer-brand{position:absolute;left:98px;width:307px;text-align:center;top:70px;font-size:24px;color:#555;white-space:nowrap}
.copyright{position:absolute;left:98px;width:307px;text-align:center;top:127px;font-size:10.5px;color:#555;white-space:nowrap}
.footer-social{position:absolute;top:170px;width:18px;height:18px;border-radius:50%;background:#555}
.footer-title{position:absolute;top:20px;font-size:22px;font-weight:600;color:var(--white);white-space:nowrap}
.footer-rule{position:absolute;top:53px;height:1px;background:#444}
.contact-item{position:absolute;left:482px;font-size:13px;color:var(--footer-text);line-height:14px;white-space:nowrap}
.contact-icon{position:absolute;left:449px;width:24px;height:24px;border-radius:50%;background:#4a4a4a}
.quick-link{position:absolute;left:840px;font-size:14px;color:var(--footer-text)}
.quick-link::before{content:"";position:absolute;left:-14px;top:5px;border-left:7px solid var(--footer-text);border-top:5px solid transparent;border-bottom:5px solid transparent}
</style>
</head>
<body>

<header class="site-header">
  <div class="brand">marvello tebani</div>
  <nav class="main-nav">
    <a class="active" href="#">Home</a>
    <a style="left:546px" href="#">About me</a>
    <a style="left:658px" href="#">Portfolio</a>
    <a style="left:777px" href="#">Blog</a>
    <a style="left:846px" href="#">Contact me</a>
  </nav>
  <span class="social" style="left:994px;top:21px" aria-label="social link"></span>
  <span class="social" style="left:1036px;top:21px" aria-label="social link"></span>
  <span class="social" style="left:1078px;top:21px" aria-label="social link"></span>
  <span class="social" style="left:1118px;top:21px" aria-label="social link"></span>
</header>

<section class="hero">
  <div class="abs" role="img" aria-label="Smiling photographer in denim shirt holding a camera, pointing to the side" style="left:780px;top:10px;width:320px;height:493px;background:linear-gradient(180deg,#b8c4d4,#8fa4c0 60%,#a6936f)"></div>
  <div class="hero-tagline">Creating Quality Photos With</div>
  <div class="hero-title">Professional Touch</div>
  <svg class="abs" style="left:32px;top:222px" width="20" height="34" viewBox="0 0 20 34"><path d="M16 3 4 17l12 14" fill="none" stroke="#1c1c1c" stroke-width="4"/></svg>
  <svg class="abs" style="left:1134px;top:222px" width="20" height="34" viewBox="0 0 20 34"><path d="M4 3l12 14L4 31" fill="none" stroke="#1c1c1c" stroke-width="4"/></svg>
  <span class="hero-dot" style="left:567px;background:var(--pink);box-shadow:0 0 0 2px #fff"></span>
  <span class="hero-dot" style="left:593px"></span>
  <span class="hero-dot" style="left:619px"></span>
</section>

<h2 class="section-title" style="left:86px;top:612px">About me</h2>
<p class="about-lead">Lorem ipsum dolor sit amet, consectetur adipiscing elit sed do eiusmod tempor incididunt.</p>
<p class="about-copy" style="top:726px">Lorem Ipsum is simply dummy text of the printing and typesetting industry. Lorem Ipsum has been the industry's standard dummy text ever since the 1500s, when an unknown printer took a galley of type and scrambled it to make a type specimen book.</p>
<p class="about-copy" style="top:814px">It has survived not only five centuries, but also the leap into electronic typesetting, remaining essentially unchanged.</p>
<p class="about-copy" style="top:870px">It was popularised in the 1960s with the release of Brightline sheets containing Lorem Ipsum passages, and more recently with desktop publishing software like Folio Layout Studio including versions of Lorem Ipsum.</p>

<h2 class="section-title" style="left:661px;top:612px">Skills</h2>
<div class="skill-label" style="top:694px">Digital Photography</div>
<div class="skill-track" style="top:728px"><div class="skill-fill" style="width:90%"></div><span class="skill-tip" style="left:90%">90%</span></div>
<div class="skill-label" style="top:754px">Analog Photography</div>
<div class="skill-track" style="top:786px"><div class="skill-fill" style="width:80%"></div><span class="skill-tip" style="left:80%">80%</span></div>
<div class="skill-label" style="top:809px">Portrait</div>
<div class="skill-track" style="top:838px"><div class="skill-fill" style="width:58%"></div><span class="skill-tip" style="left:58%">55%</span></div>
<div class="skill-label" style="top:862px">Wedding Photography</div>
<div class="skill-track" style="top:889px"><div class="skill-fill" style="width:89%"></div><span class="skill-tip" style="left:89%">89%</span></div>

<h2 class="section-title center" style="left:0;width:1200px;text-align:center;top:975px">Portfolio</h2>
<span class="filter active" style="left:86px">All</span>
<span class="filter" style="left:150px">Weddings</span>
<span class="filter" style="left:249px">Analogue</span>

<div class="tile" role="img" aria-label="Wedding detail, hands with a ring, under a pink hover overlay" style="left:0;top:1121px;width:299px;height:299px;background:linear-gradient(135deg,#e06a80,#c9425c)">
  <svg class="abs" style="left:96px;top:116px" width="84" height="70" viewBox="0 0 84 70"><rect x="2" y="22" width="44" height="44" fill="none" stroke="#fff" stroke-width="4"/><path d="M34 4h46v46" fill="none" stroke="#fff" stroke-width="4"/><path d="M24 44 78 6" stroke="#fff" stroke-width="4"/></svg>
</div>
<div class="tile" role="img" aria-label="Woman in a red dress seated in a green garden" style="left:300px;top:1121px;width:299px;height:299px;background:linear-gradient(160deg,#4f7a32,#2f4a1e 55%,#a82430)"></div>
<div class="tile" role="img" aria-label="Woman in sunglasses at the seaside" style="left:600px;top:1121px;width:299px;height:299px;background:linear-gradient(180deg,#7fb3cf,#5d9fbb 50%,#6a4b3a)"></div>
<div class="tile" role="img" aria-label="Blonde woman portrait on dark background" style="left:900px;top:1121px;width:300px;height:299px;background:linear-gradient(135deg,#1f2a38,#3a3a42 50%,#b49a6e)"></div>
<div class="tile" role="img" aria-label="Man in a suit and bow tie above a city skyline" style="left:0;top:1422px;width:861px;height:298px;background:linear-gradient(180deg,#c8cdd6,#b8866a 55%,#4a5838)"></div>
<div class="tile" role="img" aria-label="Couple embracing on a rocky shore" style="left:863px;top:1422px;width:337px;height:298px;background:linear-gradient(180deg,#b9cbd8,#8c7a58 55%,#5e5138)"></div>
<div class="tile" role="img" aria-label="Prom couple posing together" style="left:0;top:1722px;width:399px;height:299px;background:linear-gradient(135deg,#3b3430,#7a5a4a 50%,#222)"></div>
<div class="tile" role="img" aria-label="Woman in a fur collar, moody studio portrait" style="left:401px;top:1722px;width:396px;height:299px;background:linear-gradient(135deg,#4a5664,#2a323c 60%,#8b6d5c)"></div>
<div class="tile" role="img" aria-label="Woman with flowers in her hair, close portrait" style="left:799px;top:1722px;width:401px;height:299px;background:linear-gradient(135deg,#2c3550,#6a4a52 50%,#c6865e)"></div>

<h2 class="section-title center" style="left:0;width:1200px;text-align:center;top:2078px">Contact me</h2>
<form>
  <label class="field-label" style="top:2186px">Name</label><span class="field-line" style="top:2210px"></span>
  <label class="field-label" style="top:2225px">Email</label><span class="field-line" style="top:2248px"></span>
  <label class="field-label" style="top:2265px">Subject</label><span class="field-line" style="top:2288px"></span>
  <label class="field-label" style="top:2305px">Message</label><span class="field-line" style="top:2391px"></span>
  <div class="send-btn">SEND</div>
</form>
<div class="map" role="img" aria-label="Street map of central London with the studio location pinned"></div>

<footer class="site-footer">
  <div class="footer-brand">marvello tebani</div>
  <div class="copyright">Copyright © 2016 Tebani Studio. All Right Reserved.</div>
  <span class="footer-social" style="left:190px"></span>
  <span class="footer-social" style="left:215px"></span>
  <span class="footer-social" style="left:240px"></span>
  <span class="footer-social" style="left:265px"></span>

  <div class="footer-title" style="left:447px">Get in Touch</div>
  <span class="footer-rule" style="left:447px;width:225px"></span>
  <span class="contact-icon" style="top:71px"></span>
  <svg class="abs" style="left:455px;top:77px" width="12" height="12" viewBox="0 0 12 12"><path d="M2 1h3l1 3-2 1c1 2 2 3 3 3l1-2 3 1v3c-5 1-10-4-9-9z" fill="#999"/></svg>
  <div class="contact-item" style="top:76px">020 7946 0312</div>
  <span class="contact-icon" style="top:119px"></span>
  <svg class="abs" style="left:454px;top:127px" width="14" height="10" viewBox="0 0 14 10"><rect x="1" y="1" width="12" height="8" fill="none" stroke="#999" stroke-width="1.5"/><path d="M1 1l6 5 6-5" fill="none" stroke="#999" stroke-width="1.5"/></svg>
  <div class="contact-item" style="top:124px">hello@tebanistudio.co.uk</div>
  <span class="contact-icon" style="top:166px"></span>
  <svg class="abs" style="left:456px;top:170px" width="10" height="15" viewBox="0 0 10 15"><path d="M5 14S1 8 1 5a4 4 0 0 1 8 0c0 3-4 9-4 9z" fill="#999"/><circle cx="5" cy="5" r="1.5" fill="#4a4a4a"/></svg>
  <div class="contact-item" style="top:167px">Unit 4, Canal Yard<br>18 Wharf Road London N1 7RE</div>

  <div class="footer-title" style="left:823px">Quick Links</div>
  <span class="footer-rule" style="left:823px;width:276px"></span>
  <div class="quick-link" style="top:68px">Home</div>
  <div class="quick-link" style="top:91px">About Me</div>
  <div class="quick-link" style="top:114px">Portfolio</div>
  <div class="quick-link" style="top:139px">Blog</div>
  <div class="quick-link" style="top:163px">Contact Me</div>
</footer>

</body>
</html>
```